Business Cards

I'm an contractor and consultant in IT Project management. I'd like a design for business cards.
In my work I mostly meet clients, peer project managers and technical staff. I usually exchange business cards at technical conventions or when networking.
I provide services that are:
- Updated, always with a fresh look on technology
- Solid and reliable
- Flexible schedule and always available
The current business card has been attached to provide information.
Target Market(s)
IT managers, IT project managers, consultants, recruitment staff. Age 30-45 years. College/University degree.
Industry/Entity Type
Contractor
Colors
Designer to choose colors to be used in the design.
Requirements
Must have
- Two sides, one side with personal information and the other side with company name.
Text in Norwegian, including Norwegian characters
Nice to have
- It should be possible for non-Norwegian speakers to read the contact details.

```html
<!DOCTYPE html>
<html lang="no">
<head>
<meta charset="utf-8">
<title>Varden Consulting AS – visittkort</title>
<link rel="stylesheet" href="https://fonts.googleapis.com/css2?family=Noto+Serif:wght@400;700&display=swap">
<style>
  :root {
    --page-bg: #e9ebee;
    --brand-blue: #1f7fc4;
    --brand-blue-light: #3aa6e4;
    --brand-blue-deep: #0f6db5;
    --band-grey: #8c8f94;
    --ink-navy: #1d2a3a;
    --ink: #222;
    --card-white: #ffffff;
  }
  * { box-sizing: border-box; margin: 0; padding: 0; }
  html, body { width: 1200px; height: 900px; overflow: hidden; }
  body {
    background: var(--page-bg);
    font-family: "Noto Serif", "DejaVu Serif", serif;
    position: relative;
  }
  .card {
    position: absolute;
    left: 300px;
    width: 600px;
    height: 343px;
    box-shadow: 0 6px 18px rgba(0,0,0,.18);
    overflow: hidden;
  }
  .card--company { top: 88px; }
  .card--personal { top: 469px; background: var(--card-white); }

  /* Company side */
  .card--company {
    background: radial-gradient(ellipse 55% 60% at 45% 45%, var(--brand-blue-light) 0%, var(--brand-blue) 55%, var(--brand-blue-deep) 100%);
  }
  .company-block {
    position: absolute;
    left: 150px;
    top: 138px;
  }
  .company-block .company-name {
    color: #fff;
    font-size: 29px;
    font-weight: 400;
    letter-spacing: .5px;
    line-height: 1;
  }
  .company-block .company-tagline {
    color: var(--ink-navy);
    font-size: 19px;
    margin-left: 96px;
    margin-top: 2px;
  }

  /* Personal side */
  .personal-company {
    position: absolute;
    left: 40px;
    top: 34px;
  }
  .personal-company .company-name {
    color: var(--brand-blue);
    font-size: 19px;
    line-height: 1;
  }
  .personal-company .company-tagline {
    color: var(--ink);
    font-size: 15px;
    margin-left: 30px;
  }
  .contact-block {
    position: absolute;
    left: 352px;
    top: 40px;
    color: var(--ink);
  }
  .person-name { font-size: 18px; line-height: 1; letter-spacing: .5px; }
  .person-title { color: var(--brand-blue); font-size: 12px; margin-left: -4px; }
  .address { margin-top: 34px; font-size: 13px; line-height: 1.2; }
  .contact-list { list-style: none; margin-top: 34px; margin-left: -20px; }
  .contact-list li {
    display: flex; align-items: center; gap: 10px;
    font-size: 13.5px; height: 21px;
  }
  .contact-list svg { width: 14px; height: 14px; fill: var(--brand-blue); flex: none; }
  .wave { position: absolute; left: 0; bottom: 0; width: 600px; height: 343px; }
  .wave .band-grey { fill: var(--band-grey); }
  .wave .band-blue { fill: var(--brand-blue); }
</style>
</head>
<body>
  <section class="card card--company" aria-label="Forside">
    <div class="company-block">
      <div class="company-name">VARDEN CONSULTING AS</div>
      <div class="company-tagline">IT Implementering</div>
    </div>
  </section>

  <section class="card card--personal" aria-label="Bakside">
    <svg class="wave" viewBox="0 0 600 343" aria-hidden="true">
      <path class="band-grey" d="M0 238 Q 260 300 600 286 L600 343 L0 343 Z"/>
      <path class="band-blue" d="M0 252 Q 260 312 600 298 L600 343 L0 343 Z"/>
    </svg>
    <div class="personal-company">
      <div class="company-name">VARDEN CONSULTING AS</div>
      <div class="company-tagline">IT Implementering</div>
    </div>
    <div class="contact-block">
      <div class="person-name">EIRIK LUNDE</div>
      <div class="person-title">IT Rådgiver</div>
      <div class="address">Bjerkeveien 14<br>0557 Oslo</div>
      <ul class="contact-list">
        <li><svg viewBox="0 0 14 14"><path d="M4 0h6a1 1 0 0 1 1 1v12a1 1 0 0 1-1 1H4a1 1 0 0 1-1-1V1a1 1 0 0 1 1-1zm0.8 1.6v9.4h4.4V1.6z"/></svg>41527806</li>
        <li><svg viewBox="0 0 14 14"><rect x="0" y="3" width="14" height="9" rx="1"/></svg>eirik@vardenconsulting.no</li>
        <li><svg viewBox="0 0 14 14"><circle cx="7" cy="7" r="6" fill="none" stroke="#1f7fc4" stroke-width="1.2"/><ellipse cx="7" cy="7" rx="2.6" ry="6" fill="none" stroke="#1f7fc4" stroke-width="1"/><path d="M1 7h12" stroke="#1f7fc4" stroke-width="1"/></svg>www.vardenconsulting.no</li>
      </ul>
    </div>
  </section>
</body>
</html>
```